Travel Consultant Business Card

Hello.. New travel consultant looking seeking a business card that incorporates my new logo. I specialize in cruises but also want to imply land vacation. I am very open to any design and font concepts. I'm looking for a very upbeat modern design that reflects cruise and land vacations. Bright vibrant colors

Target Market(s)

Cruise and Land Vacationers

Industry/Entity Type

Travel Agent

Contact Information for Business Card

I am very open to any design and font concepts. I'm looking for a very upbeat modern design that reflects cruise and land vacations. Bright vibrant colors

Colors

Designer to choose colors to be used in the design.

Requirements
Must have
• Company Name: PineRidge Journeys---New logo uploaded to be included in design
• My Name: Danielle Marchetti-Travel Consultant
• Phone Number: (555) 418-7093
• E-Mail Address: pineridgejourneys@mailbox-example.com
• Website: www.pineridgejourneys-example.com
Nice to have
• My tag line is …..Here to Get You There

```html
<!DOCTYPE html>
<html lang="en">
<head>
<meta charset="utf-8">
<title>PineRidge Journeys – Business Card</title>
<link href="https://fonts.googleapis.com/css2?family=Roboto:wght@400;500;700&family=Sacramento&display=swap" rel="stylesheet">
<style>
  :root {
    --backdrop: #e9e6e1;
    --card-white: #ffffff;
    --brand-navy: #2d4fa6;
    --brand-blue: #1f5fb0;
    --brand-sky: #3aa2dc;
    --card-blue: #1664b3;
    --text-dark: #2a3f8f;
    --sea-deep: #0f5c9c;
    --sea-light: #3fa9c9;
    --sky-top: #a9d3ef;
    --grass: #5d9a3a;
  }
  * { box-sizing: border-box; margin: 0; padding: 0; }
  html, body {
    width: 900px; height: 1200px; overflow: hidden;
    background: var(--backdrop);
    font-family: "Roboto", Arial, sans-serif;
  }
  .canvas { position: relative; width: 900px; height: 1200px; }

  .card {
    position: absolute; left: 85px; width: 733px; height: 429px;
    border-radius: 22px; overflow: hidden;
    box-shadow: 0 6px 14px rgba(0,0,0,0.25);
  }
  .card--front { top: 143px; background: var(--card-white); }
  .card--back { top: 633px; background: var(--card-blue); }

  .scene-photo {
    position: absolute; left: 265px; top: 0; width: 468px; height: 429px;
    background:
      linear-gradient(180deg, var(--sky-top) 0%, #d9ecf8 32%, var(--sea-deep) 36%, #1d74b4 60%, var(--sea-light) 82%, var(--grass) 95%, #4c8a2e 100%);
    -webkit-mask-image: linear-gradient(90deg, transparent 0%, #000 32%);
    mask-image: linear-gradient(90deg, transparent 0%, #000 32%);
  }

  .brand-name {
    position: absolute; font-weight: 700; letter-spacing: -0.5px; white-space: nowrap;
  }
  .card--front .brand-name {
    left: 50px; top: 62px; font-size: 35px; color: var(--brand-blue);
  }
  .card--back .brand-name {
    left: 0; right: 0; top: 170px; text-align: center; font-size: 44px; color: #ffffff;
  }

  .person { position: absolute; left: 51px; top: 240px; }
  .person__name { font-size: 23px; font-weight: 500; color: var(--text-dark); }
  .person__title { font-size: 17px; color: var(--brand-sky); margin-top: 4px; }

  .contact-list { position: absolute; left: 52px; top: 306px; list-style: none; }
  .contact-list li {
    display: flex; align-items: center; height: 27.5px;
    font-size: 16px; color: var(--text-dark); white-space: nowrap;
  }
  .contact-list svg { width: 18px; height: 18px; margin-right: 14px; flex: none; }

  .tagline {
    position: absolute; left: 0; right: 0; top: 358px; text-align: center;
    font-family: "Sacramento", cursive; font-size: 34px; color: #ffffff;
  }
</style>
</head>
<body>
<div class="canvas">

  <section class="card card--front">
    <div class="scene-photo" role="img" aria-label="Photo of a white cruise ship sailing past a green island on a bright blue sea, grass in the foreground"></div>

    <div class="brand-name">PineRidge Journeys</div>

    <div class="person">
      <div class="person__name">Danielle Marchetti</div>
      <div class="person__title">Travel Consultant</div>
    </div>

    <ul class="contact-list">
      <li>
        <svg viewBox="0 0 24 24" fill="var(--brand-sky)"><path d="M6.6 10.8a15.1 15.1 0 0 0 6.6 6.6l2.2-2.2c.3-.3.7-.4 1-.2 1.1.4 2.3.6 3.6.6.6 0 1 .4 1 1V20c0 .6-.4 1-1 1A17 17 0 0 1 3 4c0-.6.4-1 1-1h3.5c.6 0 1 .4 1 1 0 1.3.2 2.5.6 3.6.1.3 0 .7-.2 1z"/></svg>
        (555) 418-7093
      </li>
      <li>
        <svg viewBox="0 0 24 24" fill="none" stroke="var(--brand-sky)" stroke-width="2"><rect x="3" y="5" width="18" height="14"/><path d="M3 5l9 8 9-8"/></svg>
        pineridgejourneys@mailbox-example.com
      </li>
      <li>
        <svg viewBox="0 0 24 24" fill="none" stroke="var(--brand-sky)" stroke-width="1.8"><circle cx="12" cy="12" r="9"/><ellipse cx="12" cy="12" rx="4" ry="9"/><path d="M3 12h18M5 7h14M5 17h14"/></svg>
        www.pineridgejourneys-example.com
      </li>
    </ul>
  </section>

  <section class="card card--back">
    <div class="brand-name">PineRidge Journeys</div>
    <div class="tagline">Here to Get You There</div>
  </section>

</div>
</body>
</html>
```